Brisk. Technology Logistics Software platform.

A modern looking and feeling website for a logistics software platform.
We connect retailers or wholesale parcel distributors to worldwide delivery solutions.
Methods tend to be road and air transport to final mile courier companies and post offices all over the world.
Our platform is for ecommerce distribution. A customer uses BRISK to enable them to connect to worldwide companies who will track and trace the delivery of their goods.

Target Market(s)

Onllne retailers. Markert Places such as Tolvaro and Quendix. Wholesale third party logistics and packaging companies. Delivery companies based in the UK looking to expand overseas.

Number of Pages Required

5+ page

Font styles to use
Sans Serif

Colors
aaaaaa
dbdbdb
e6e6e6
c4c4c4
cbcbcb
c9c9c9
ec1f27
3176b5
0355a3

Requirements
Must have
• Landing Page.
• What we do.
• Who we are.
• Modules.
• Testimonies (password protected)
• Contact us.
• Interactive for mobile operating systems.
• Scrolling website.
• Short stock video showing on key pages.
• Very well polished fonts and buttons. A sharp and well executed website is required.
• Simplicity in feeling.
• To the point on message.
• Refined wording and copyrighting / messaging
• A link to our sub brand and product Brisk Parcels
• Capture interest so people read further.
Nice to have
• A polished video to explain what we do on landing page. Clipmarrow.net have some good options but not sure how professional they will look.
Should not have
• Bad graphics and colours.
• Not lots of clicks. Less as possible
• Complex message

```html
<!DOCTYPE html>
<html lang="en">
<head>
<meta charset="utf-8">
<title>Brisk. Technology — Home</title>
<link href="https://fonts.googleapis.com/css2?family=Poppins:wght@400;500;600;700&display=swap" rel="stylesheet">
<style>
:root{
  --red:#ec1f27;
  --blue:#0355a3;
  --blue-mid:#3176b5;
  --ink:#3a3a3a;
  --muted:#6b6b6b;
  --header-bg:#f1f1f1;
  --panel:#f5f5f5;
  --dash:#aaaaaa;
  --footer:#46443d;
  --footer-line:#8a877f;
  --white:#ffffff;
}
*{margin:0;padding:0;box-sizing:border-box}
html,body{width:1200px;height:1200px;overflow:hidden;background:var(--white)}
body{font-family:'Poppins',sans-serif;position:relative}
.page{position:absolute;left:254px;top:0;width:864px;height:1500px;transform:scale(.8);transform-origin:0 0;background:var(--white);overflow:hidden}
.abs{position:absolute}

/* header */
.site-header{left:0;top:0;width:864px;height:50px;background:var(--header-bg);z-index:3}
.brand{left:72px;top:12px;font-size:19px;font-weight:600;color:var(--red);letter-spacing:.2px;line-height:24px}
.nav{top:0;left:0;height:50px;width:864px}
.nav a{position:absolute;top:21px;font-size:10px;font-weight:500;color:var(--ink);text-decoration:none;letter-spacing:.2px;white-space:nowrap}
.nav a.active{color:var(--ink)}
.nav a.active::after{content:"";position:absolute;left:-3px;right:-3px;top:26px;height:2px;background:var(--red)}
.caret{display:inline-block;width:5px;height:5px;border-right:1px solid var(--ink);border-bottom:1px solid var(--ink);transform:rotate(45deg);margin-left:6px;position:relative;top:-2px}

/* hero */
.hero{left:0;top:50px;width:864px;height:440px;clip-path:polygon(0 0,100% 0,100% 100%,0 335px);
  background:linear-gradient(100deg,#2a1416 0%,#5a2426 35%,#b9494c 62%,#8d3436 80%,#5a2a2b 100%)}
.hero-title{left:0;width:864px;top:100px;text-align:center;color:var(--white);font-size:15.5px;font-weight:500;line-height:30px;letter-spacing:.1px}
.play{left:316px;top:202px;width:68px;height:68px;border:2.5px solid var(--white);border-radius:50%}
.play svg{position:absolute;left:24px;top:20px}
.btn{position:absolute;display:flex;align-items:center;justify-content:center;border-radius:20px;font-size:11.5px;font-weight:500;letter-spacing:.2px;white-space:nowrap}
.btn-quote{left:423px;top:217px;width:150px;height:37px;background:var(--white);color:var(--red)}
.btn-quote svg{margin-left:12px}

/* what we do */
.photo{background:linear-gradient(160deg,#8a9bb3,#d7c84a 45%,#3f3f3f 100%)}
.photo-forklift{left:71px;top:468px;width:145px;height:235px;background:linear-gradient(165deg,#5b6f92 0%,#c8c23a 40%,#e8e3cc 70%,#8b8b8b 100%)}
.photo-truck{left:228px;top:557px;width:145px;height:235px;background:linear-gradient(170deg,#4e78b8 0%,#dfe6ee 35%,#d4262a 60%,#8a8a8a 100%)}
.section-bar{left:432px;top:572px;width:2px;height:33px;background:var(--blue)}
.section-title{left:446px;top:578px;font-size:14px;font-weight:700;color:var(--blue);letter-spacing:.4px}
.copy{left:432px;width:360px;font-size:8.6px;line-height:15px;color:var(--muted);text-transform:uppercase;text-align:justify}

/* containers band */
.band{left:0;top:786px;width:864px;height:274px;clip-path:polygon(0 101px,100% 0,100% 100%,0 100%);
  background:linear-gradient(95deg,#4a4036 0%,#6a5a48 30%,#3a3d45 55%,#5a4a40 75%,#2d3a4a 100%)}
.band::after{content:"";position:absolute;inset:0;background:rgba(20,20,25,.35)}
.band-title{left:0;width:864px;top:902px;text-align:center;color:var(--white);font-size:15.5px;font-weight:500;line-height:25px}
.btn-parcel{left:296px;top:969px;width:132px;height:39px;background:var(--red);color:var(--white)}
.btn-tech{left:439px;top:969px;width:169px;height:39px;background:var(--white);color:var(--red)}
.btn .plus{width:13px;height:13px;border-radius:50%;margin-right:10px;position:relative;flex:none}
.btn-parcel .plus{background:var(--white)}
.btn-tech .plus{background:var(--red)}
.plus::before,.plus::after{content:"";position:absolute;left:50%;top:50%;transform:translate(-50%,-50%)}
.plus::before{width:7px;height:1.6px}
.plus::after{width:1.6px;height:7px}
.btn-parcel .plus::before,.btn-parcel .plus::after{background:var(--red)}
.btn-tech .plus::before,.btn-tech .plus::after{background:var(--white)}

/* tracking */
.track{left:72px;top:1098px;width:720px;height:146px;background:var(--panel);border:1.5px dashed var(--dash)}
.track-title{left:0;width:100%;top:25px;text-align:center;font-size:15px;color:#555;letter-spacing:.2px}
.track-arrow{left:354px;top:56px}
.btn-track{left:291px;top:82px;width:134px;height:38px;background:var(--blue);color:var(--white)}
.btn-track svg{margin-right:8px}

/* footer */
.site-footer{left:0;top:1281px;width:864px;height:219px;background:var(--footer);color:var(--white)}
.f-head{top:22px;font-size:12px;font-weight:500;letter-spacing:.2px;display:flex;align-items:center;white-space:nowrap}
.f-head span.rule{display:block;height:1px;background:var(--footer-line);margin-left:9px}
.f-text{left:72px;top:50px;font-size:9.6px;line-height:15.2px;color:#e8e8e8;width:210px}
.btn-msg{position:absolute;left:72px;top:121px;width:115px;height:27px;background:var(--white);color:var(--ink);font-size:9.2px;display:flex;align-items:center;justify-content:center}
.socials{left:368px;top:54px;display:flex;gap:13px}
.socials i{display:block;width:11px;height:11px;background:#e8e8e8;border-radius:2px}
.links{left:622px;top:51px;font-size:9.6px;line-height:14.2px;color:#e8e8e8;list-style:none}
.f-divider{left:72px;top:171px;width:720px;height:1px;background:var(--footer-line)}
.copyright{left:0;width:864px;top:190px;text-align:center;font-size:8.6px;color:#e0e0e0}
</style>
</head>
<body>
<main class="page">

  <header class="site-header abs">
    <div class="brand abs">Brisk. Technology</div>
    <nav class="nav abs">
      <a class="active" style="left:386px">HOME</a>
      <a style="left:447px">SOLUTIONS<span class="caret"></span></a>
      <a style="left:544px">TESTIMONIAL LOGIN<span class="caret"></span></a>
      <a style="left:677px">FAQS</a>
      <a style="left:735px">CONTACT US</a>
    </nav>
  </header>

  <section class="hero abs" role="img" aria-label="Red-tinted photo of a delivery truck parked at a loading dock"></section>
  <h1 class="hero-title abs">BRISK. TECHNOLOGY AND PARCEL SOLUTIONS BUILT TO HELP DEVELOP<br>&amp; MANAGE YOUR GLOBAL DELIVERY NETWORK</h1>
  <div class="play abs">
    <svg width="22" height="26" viewBox="0 0 22 26"><path d="M0 0 L22 13 L0 26 Z" fill="#fff"/></svg>
  </div>
  <a class="btn btn-quote">GET A QUOTE
    <svg width="10" height="12" viewBox="0 0 10 12"><path d="M5 11 V1 M1 5 L5 1 L9 5" stroke="#ec1f27" stroke-width="1.8" fill="none"/></svg>
  </a>

  <div class="photo-forklift abs" role="img" aria-label="Photo of a warehouse worker driving a yellow forklift"></div>
  <div class="photo-truck abs" role="img" aria-label="Photo of a red lorry beside stacked shipping containers with a plane overhead"></div>
  <div class="section-bar abs"></div>
  <h2 class="section-title abs">WHAT WE DO</h2>
  <p class="copy abs" style="top:623px">Working closely with ecommerce, Brisk. Technology have developed solutions purely focused on delivering what's required within the global delivery marketplace. Meeting all needs and more for retailers and global delivery solution providers</p>
  <p class="copy abs" style="top:691px">Allowing customers to grow at a fast pace; most importantly providing tools to help them manage their global delivery network supported by "dynamic real time visibility" management tools</p>

  <section class="band abs" role="img" aria-label="Photo of a container port with stacked shipping containers and workers"></section>
  <h2 class="band-title abs">ENSURING SOLUTIONS EVOLVE TO SUIT OUR CUSTOMERS BUSINESS<br>REQUIREMENTS</h2>
  <a class="btn btn-parcel"><span class="plus"></span>BRISK PARCEL</a>
  <a class="btn btn-tech"><span class="plus"></span>BRISK TECHNOLOGY</a>

  <section class="track abs">
    <p class="track-title abs">YOU CAN TRACK YOUR PARCEL HERE</p>
    <svg class="track-arrow abs" width="10" height="12" viewBox="0 0 10 12"><path d="M5 0 V10 M1 6 L5 10 L9 6" stroke="#333" stroke-width="1.4" fill="none"/></svg>
    <a class="btn btn-track">
      <svg width="13" height="13" viewBox="0 0 13 13"><path d="M13 0 L0 6 L6 7 L7 13 Z" fill="#fff"/></svg>TRACK PARCEL
    </a>
  </section>

  <footer class="site-footer abs">
    <div class="f-head abs" style="left:72px">SEND US A MESSAGE<span class="rule" style="width:85px"></span></div>
    <div class="f-head abs" style="left:368px">WE ARE SOCIAL<span class="rule" style="width:86px"></span></div>
    <div class="f-head abs" style="left:622px">QUICK LINKS<span class="rule" style="width:85px"></span></div>
    <p class="f-text abs">Interested in connecting to explore how Brisk Ltd can work for your business Message us we'll connect you with the right person</p>
    <a class="btn-msg">CLICK TO MESSAGE</a>
    <div class="socials abs" aria-label="Social links"><i></i><i></i><i></i></div>
    <ul class="links abs">
      <li>- About us</li>
      <li>- Terms and Conditions</li>
      <li>- Privacy Policy</li>
      <li>- Site Map</li>
    </ul>
    <div class="f-divider abs"></div>
    <p class="copyright abs">© Copyrights 2018. All Rights Reserved.</p>
  </footer>

</main>
</body>
</html>
```